Electrician Company Website Design

I am looking to get a website designed only. I do not need it converted ot html. I simply need the design in a psd format. I have my own team for the conversion. The website is for an electrician company called Bramblecourt electric. I have created a txt document with the project parameters and specifics. I have also uploaded their logo in all avaible formats. It's a zip file.

Number of Pages Required

1 page

```html
<!DOCTYPE html>
<html lang="en">
<head>
<meta charset="utf-8">
<title>Bramblecourt Electric</title>
<link href="https://fonts.googleapis.com/css2?family=Poppins:wght@400;500;600;700;800&display=swap" rel="stylesheet">
<style>
:root{
  --blue:#1f64b0;
  --blue-dark:#14539c;
  --red:#e0161f;
  --red-dark:#c8141c;
  --ink:#111;
  --black:#050505;
  --white:#fff;
}
*{box-sizing:border-box;margin:0;padding:0}
html,body{width:711px;height:1200px;overflow:hidden;background:var(--white)}
body{position:relative;font-family:'Poppins',sans-serif;color:var(--ink)}
.abs{position:absolute}

/* header */
.topbar{top:9px;right:0;display:flex;align-items:center;gap:0;font-weight:600}
.topbar-address{left:445px;top:10px;font-size:7px;line-height:8.5px;color:var(--red);display:flex;gap:10px;align-items:center}
.topbar-phone{left:556px;top:9px;font-size:13px;color:var(--red);display:flex;gap:10px;align-items:center}
.brand{left:35px;top:36px;display:flex;align-items:center;gap:10px}
.brand-mark{width:22px;height:22px;border-radius:50%;background:var(--blue)}
.brand-name{font-weight:700;font-size:12.5px;line-height:15px;color:var(--ink);text-transform:uppercase;width:110px}
.brand-name{position:absolute;left:117px;top:42px}
.nav{left:295px;top:44px;display:flex;gap:22px;font-size:9px;font-weight:500}
.nav a{color:var(--ink);text-decoration:none}
.nav a.active{color:var(--blue);border-bottom:2px solid var(--blue);padding-bottom:1px}

/* hero */
.hero{left:0;top:93px;width:711px;height:271px;background:radial-gradient(circle at 40% 30%,#2a1a12 0%,#0a0706 55%,#000 100%);overflow:hidden}
.hero-photo{position:absolute;left:409px;top:15px;width:420px;height:420px;border-radius:50%;background:linear-gradient(135deg,#b8c4cf 0%,#8fa0b0 45%,#c43226 70%,#9a2a22 100%)}
.hero-title{left:46px;top:42px;color:var(--white);font-size:29px;line-height:38px;font-weight:500}
.hero-title strong{font-weight:800;display:inline-flex;align-items:flex-end;gap:10px}
.hero-title strong span{display:inline-block;width:73px;height:2px;background:var(--white);margin-bottom:8px}
.hero-copy{left:50px;top:162px;color:var(--white);font-size:7.8px;line-height:18.5px;font-weight:500}
.btn-learn{left:50px;top:218px;width:86px;height:23px;background:var(--red);color:var(--white);font-size:9px;font-weight:700;border-radius:4px;display:flex;align-items:center;justify-content:center;box-shadow:0 0 12px rgba(224,22,31,.7)}

/* info cards */
.card{width:159px;height:192px;border-radius:16px;color:var(--white);padding:26px 21px}
.card.blue{background:linear-gradient(160deg,#2a6fb8,#1a5aa3)}
.card.red{background:linear-gradient(160deg,#e11d25,#c4151d)}
.card h3{font-size:12px;font-weight:700;letter-spacing:.3px;margin-bottom:9px}
.card p{font-size:7.6px;line-height:18.5px;font-weight:500}
.card .rule{width:46px;height:2px;background:var(--white);margin-top:6px}
.dots{display:grid;gap:5px}
.dots i{display:block;width:5px;height:5px;border-radius:50%}

.btn-services{left:304px;top:604px;width:103px;height:28px;border-radius:4px;background:var(--blue);color:var(--white);font-size:9px;font-weight:700;display:flex;align-items:center;justify-content:center;letter-spacing:.4px}

/* services band */
.band{left:0;top:650px;width:711px;height:231px}
.svc{top:650px;width:159px;height:192px;border-radius:16px;color:var(--white);padding:42px 21px 0 21px}
.svc.red{background:linear-gradient(160deg,#e7262b,#cc161d)}
.svc.blue{background:linear-gradient(160deg,#2d76c4,#1f64b0)}
.svc svg.ico{display:block;margin-bottom:10px}
.svc h4{font-size:12px;line-height:18.5px;font-weight:700;letter-spacing:.4px}
.svc .rule{width:46px;height:2px;background:var(--white);margin-top:8px}
.go{width:29px;height:29px;border-radius:50%;background:var(--white);display:flex;align-items:center;justify-content:center;top:732px}

/* service areas */
.areas-title{left:35px;top:917px;font-size:22.5px;font-weight:800;color:var(--blue);letter-spacing:.3px}
.areas-rule{left:35px;top:947px;width:97px;height:3px;background:var(--red)}
.areas-copy{left:35px;top:958px;font-size:9.2px;line-height:18.5px;width:360px}
.areas-list{left:35px;top:1005px;display:grid;grid-template-columns:137px 137px;row-gap:5px}
.areas-list li{list-style:none;display:flex;align-items:center;gap:6px;font-size:10.5px;font-weight:700;color:var(--blue);height:16px}
.map{left:446px;top:890px;width:158px;height:192px;background:linear-gradient(180deg,#f4f4f4,#e7e7e7);border-radius:4px}

/* footer */
.footer{left:0;top:1098px;width:711px;height:102px;background:linear-gradient(90deg,#1a5ba7,#1f64b0 60%,#1a5ba7);color:var(--white)}
.f-brand{left:36px;top:1135px;display:flex;align-items:center;gap:10px}
.f-brand .brand-mark{background:var(--white);width:20px;height:20px}
.f-brand .name{font-size:12.5px;line-height:15px;font-weight:700;text-transform:uppercase}
.f-head{font-size:8.6px;font-weight:700;letter-spacing:.3px}
.f-links{font-size:6.3px;line-height:12px;font-weight:500;margin-top:6px}
.f-phone{font-size:10.5px;font-weight:700;display:flex;gap:6px;align-items:center;margin-top:10px}
.socials{display:flex;gap:7px;margin:10px 0 0 7px}
.socials i{width:10px;height:10px;border-radius:50%;background:var(--white);display:block}
.f-office{font-size:8.6px;line-height:12px;font-weight:500}
</style>
</head>
<body>

<header>
  <div class="abs topbar-address">
    <svg width="7" height="10" viewBox="0 0 10 14"><path d="M5 0a5 5 0 0 0-5 5c0 4 5 9 5 9s5-5 5-9a5 5 0 0 0-5-5zm0 7a2 2 0 1 1 0-4 2 2 0 0 1 0 4z" fill="#1f64b0"/></svg>
    <span>1742 LARKFIELD AVE NE<br>HARROWBY, MN 55090</span>
  </div>
  <div class="abs topbar-phone">
    <svg width="11" height="11" viewBox="0 0 24 24"><path d="M6.6 10.8a15 15 0 0 0 6.6 6.6l2.2-2.2a1 1 0 0 1 1-.25 11.4 11.4 0 0 0 3.6.6 1 1 0 0 1 1 1V20a1 1 0 0 1-1 1A17 17 0 0 1 3 4a1 1 0 0 1 1-1h3.5a1 1 0 0 1 1 1c0 1.25.2 2.45.6 3.6a1 1 0 0 1-.25 1z" fill="#1f64b0"/></svg>
    <span>(555-014-2870)</span>
  </div>
  <div class="abs brand" style="top:49px"><i class="brand-mark"></i></div>
  <div class="brand-name">Bramblecourt Electric</div>
  <nav class="abs nav">
    <a href="#">COMPANY</a><a href="#">SERVICES</a><a href="#" class="active">SERVICES AREA</a><a href="#">CONTACT</a><a href="#">GALLERY</a><a href="#">FAQS</a>
  </nav>
</header>

<section class="abs hero">
  <div class="hero-photo" role="img" aria-label="Smiling electrician in red cap and shirt standing in front of a wall of electrical supplies"></div>
  <h1 class="abs hero-title">QUICK ELECTRICITY<br><strong>SERVICES <span></span></strong><br>NEAR YOUR HOUSE.</h1>
  <p class="abs hero-copy">Lorem ipsum dolor sit amet, consectetur adipiscing elit, sed<br>do eiusmod tempor incididunt ut labore et dolors.</p>
  <div class="abs btn-learn">LEARN MORE</div>
</section>

<div class="abs dots" style="left:37px;top:399px;grid-template-columns:repeat(4,5px)">
  <i style="background:var(--blue)"></i><i style="background:var(--blue)"></i><i style="background:var(--blue)"></i><i style="background:var(--blue)"></i>
  <i style="background:var(--blue)"></i><i style="background:var(--blue)"></i><i style="background:var(--blue)"></i><i></i>
  <i style="background:var(--blue)"></i><i style="background:var(--blue)"></i><i></i><i></i>
  <i style="background:var(--blue)"></i><i></i><i></i><i></i>
</div>
<div class="abs dots" style="left:640px;top:545px;grid-template-columns:repeat(4,5px)">
  <i></i><i></i><i></i><i style="background:var(--red)"></i>
  <i></i><i></i><i style="background:var(--red)"></i><i style="background:var(--red)"></i>
  <i></i><i style="background:var(--red)"></i><i style="background:var(--red)"></i><i style="background:var(--red)"></i>
  <i style="background:var(--red)"></i><i style="background:var(--red)"></i><i style="background:var(--red)"></i><i style="background:var(--red)"></i>
</div>

<article class="abs card blue" style="left:99px;top:389px">
  <h3>ABOUT US...</h3>
  <p>Lorem ipsum dolor sit amet, consectetur adipiscing elit, sed do eiusmod tempor incididunt ut labore et dolore magna aliqua. Quis maecenas accumsan lacus vel facilisis.</p>
  <div class="rule"></div>
</article>
<article class="abs card red" style="left:276px;top:389px">
  <h3>SERVICE AREAS</h3>
  <p>Lorem ipsum dolor sit amet, consectetur adipiscing elit, sed do eiusmod tempor incididunt ut labore et dolore magna aliqua. Quis maecenas accumsan lacus vel facilisis.</p>
  <div class="rule"></div>
</article>
<article class="abs card blue" style="left:453px;top:389px">
  <h3>CONTACT US...</h3>
  <p>Lorem ipsum dolor sit amet, consectetur adipiscing elit, sed do eiusmod tempor incididunt ut labore et dolore magna aliqua. Quis maecenas accumsan lacus vel facilisis.</p>
  <div class="rule"></div>
</article>

<div class="abs btn-services">OUR SERVICES</div>

<svg class="abs band" viewBox="0 0 711 231" role="img" aria-label="Dark backdrop with glowing light bulbs">
  <defs><linearGradient id="bandFill" x1="0" y1="0" x2="0" y2="1"><stop offset="0" stop-color="#050505"/><stop offset="1" stop-color="#1c130d"/></linearGradient></defs>
  <path d="M0 95 Q355 -50 711 95 L711 231 L0 231 Z" fill="url(#bandFill)"/>
</svg>

<article class="abs svc red" style="left:99px">
  <svg class="ico" width="30" height="36" viewBox="0 0 30 36" fill="none" stroke="#fff" stroke-width="1.4"><rect x="2" y="12" width="26" height="22"/><path d="M15 16l-6 12h12z"/><path d="M15 20l-2 4h4l-2 4"/><path d="M7 12V4M15 12V4M23 12V4M4 6h6M12 6h6M20 6h6M4 9h6M12 9h6M20 9h6"/></svg>
  <h4>COMMERICAL<br>ELECTRICAL<br>SERVICES</h4>
  <div class="rule"></div>
</article>
<article class="abs svc blue" style="left:276px;padding-left:25px">
  <svg class="ico" width="38" height="36" viewBox="0 0 38 36" fill="none" stroke="#fff" stroke-width="1.4"><path d="M4 2v8M8 2v8M2 10h8v6a2 2 0 0 1-4 0v10a6 6 0 0 0 6 6h6"/><path d="M12 20l12-11 12 11M15 17v15h18V17"/><path d="M25 18l-4 7h5l-3 6"/></svg>
  <h4>RESIDENTIAL<br>ELECTRICAL<br>SERVICES</h4>
  <div class="rule"></div>
</article>
<article class="abs svc red" style="left:453px;padding-left:25px">
  <svg class="ico" width="30" height="34" viewBox="0 0 30 34" fill="none" stroke="#fff" stroke-width="1.4"><rect x="2" y="2" width="26" height="26" rx="2"/><rect x="7" y="6" width="16" height="18"/><path d="M15 8l-3 5h5l-3 5"/><path d="M11 20h8M6 28v4M12 28v4M18 28v4M24 28v4"/></svg>
  <h4>INDUSTRIAL<br>ELECTRICAL<br>SERVICES</h4>
  <div class="rule"></div>
</article>

<div class="abs go" style="left:243px"><svg width="11" height="13" viewBox="0 0 11 13"><path d="M2 1l6 5.5L2 12" stroke="#1f64b0" stroke-width="3" fill="none"/></svg></div>
<div class="abs go" style="left:420px"><svg width="11" height="13" viewBox="0 0 11 13"><path d="M2 1l6 5.5L2 12" stroke="#e0161f" stroke-width="3" fill="none"/></svg></div>
<div class="abs go" style="left:598px"><svg width="11" height="13" viewBox="0 0 11 13"><path d="M2 1l6 5.5L2 12" stroke="#1f64b0" stroke-width="3" fill="none"/></svg></div>

<section>
  <h2 class="abs areas-title">SERVICE AREAS</h2>
  <div class="abs areas-rule"></div>
  <p class="abs areas-copy">Lorem ipsum dolor sit amet, consectetur adipiscing elit, sed do eiusmod tempor incididunt ut labore et dolors.</p>
  <ul class="abs areas-list">
    <li><svg width="9" height="12" viewBox="0 0 10 14"><path d="M5 0a5 5 0 0 0-5 5c0 4 5 9 5 9s5-5 5-9a5 5 0 0 0-5-5zm0 7a2 2 0 1 1 0-4 2 2 0 0 1 0 4z" fill="#e0161f"/></svg>DAKOTA</li>
    <li><svg width="9" height="12" viewBox="0 0 10 14"><path d="M5 0a5 5 0 0 0-5 5c0 4 5 9 5 9s5-5 5-9a5 5 0 0 0-5-5zm0 7a2 2 0 1 1 0-4 2 2 0 0 1 0 4z" fill="#e0161f"/></svg>CHISAGO MN</li>
    <li><svg width="9" height="12" viewBox="0 0 10 14"><path d="M5 0a5 5 0 0 0-5 5c0 4 5 9 5 9s5-5 5-9a5 5 0 0 0-5-5zm0 7a2 2 0 1 1 0-4 2 2 0 0 1 0 4z" fill="#e0161f"/></svg>GOODHUE</li>
    <li><svg width="9" height="12" viewBox="0 0 10 14"><path d="M5 0a5 5 0 0 0-5 5c0 4 5 9 5 9s5-5 5-9a5 5 0 0 0-5-5zm0 7a2 2 0 1 1 0-4 2 2 0 0 1 0 4z" fill="#e0161f"/></svg>BENTON</li>
    <li><svg width="9" height="12" viewBox="0 0 10 14"><path d="M5 0a5 5 0 0 0-5 5c0 4 5 9 5 9s5-5 5-9a5 5 0 0 0-5-5zm0 7a2 2 0 1 1 0-4 2 2 0 0 1 0 4z" fill="#e0161f"/></svg>WASHINGTON MN</li>
    <li><svg width="9" height="12" viewBox="0 0 10 14"><path d="M5 0a5 5 0 0 0-5 5c0 4 5 9 5 9s5-5 5-9a5 5 0 0 0-5-5zm0 7a2 2 0 1 1 0-4 2 2 0 0 1 0 4z" fill="#e0161f"/></svg>DOODGE</li>
  </ul>
  <div class="abs map" role="img" aria-label="County outline map of Minnesota with service locations marked"></div>
</section>

<footer class="abs footer"></footer>
<div class="abs f-brand"><i class="brand-mark"></i><span class="name">Bramblecourt<br>Electric</span></div>
<div class="abs" style="left:269px;top:1118px;color:#fff">
  <div class="f-head">COMPANY</div>
  <div class="f-links">About us<br>Services<br>Service Area<br>Company</div>
</div>
<div class="abs" style="left:377px;top:1118px;color:#fff">
  <div class="f-head">CONTACT US</div>
  <div class="f-phone"><svg width="11" height="11" viewBox="0 0 24 24"><path d="M6.6 10.8a15 15 0 0 0 6.6 6.6l2.2-2.2a1 1 0 0 1 1-.25 11.4 11.4 0 0 0 3.6.6 1 1 0 0 1 1 1V20a1 1 0 0 1-1 1A17 17 0 0 1 3 4a1 1 0 0 1 1-1h3.5a1 1 0 0 1 1 1c0 1.25.2 2.45.6 3.6a1 1 0 0 1-.25 1z" fill="#fff"/></svg>(555-014-2871)</div>
  <div class="socials"><i></i><i></i><i></i><i></i></div>
</div>
<div class="abs" style="left:504px;top:1118px;color:#fff">
  <div class="f-head">VISIT OUR HOME OFFICE</div>
  <div class="f-office" style="display:flex;gap:14px;margin-top:9px;margin-left:-20px;align-items:center">
    <svg width="8" height="11" viewBox="0 0 10 14"><path d="M5 0a5 5 0 0 0-5 5c0 4 5 9 5 9s5-5 5-9a5 5 0 0 0-5-5zm0 7a2 2 0 1 1 0-4 2 2 0 0 1 0 4z" fill="#fff"/></svg>
    <span>1742 Larkfield Ave NE<br>Harrowby, MN 55090</span>
  </div>
  <div class="f-office" style="display:flex;gap:13px;margin-top:7px;margin-left:-20px;align-items:center">
    <svg width="9" height="7" viewBox="0 0 12 9"><rect width="12" height="9" fill="#fff"/><path d="M0 0l6 5 6-5" stroke="#1f64b0" fill="none"/></svg>
    <span>hello@bramblecourt.example</span>
  </div>
</div>

</body>
</html>
```